Packaging design for aloe lotion bottle for a Laser Clinic

We need a packaging design for a body lotion bottle. Our business is a laser clinic and we are looking at slowly rolling out a range of skincare products. This lotion bottle is the first item with more to follow so the winning designer will have other designs to work on in the future.

The design needs to be classy, elegant, strong and sophisticated. The bottle will be clear with a shiny silver sleeved lid. The lotion itself, which will be visible through the bottle, will be a very light green colour. Think Mirelle Davonne and Voriel as that is the image I want to convey.

Ideally we were thinking of having a design with a single colour but if you come up with a fantastic multi colour design that we love then we're open to it.

Reason: I have extended the deadline as I feel I need more time to allow designers to submit their designs. I haven't found a design that I love just yet. The project has been made a guaranteed payment upon completion. Thank you.

Target Market(s)

upper class high income earners with a high disposable income. People that look after themselves

Industry/Entity Type

Beauty Salon

Colors
000000
cadf82

Requirements
Must have
• must include the details below:
• Post Laser Calming Cream
• This soothing and calming anti inflammatory cream is specifically formulated for use after post laser treatments.
• Fresh Cucumber, Melon and Aloe Vera Leaf Juice blend together in perfect harmony to quickly cool you skin and restore your skins natural moisture.
• Our luxurious calming cream targets redness and helps to reduce inflammation, bringing you supple and radiant skin like never before.
• Directions: Use a liberal amount twice daily on all your treatment areas. This nourishing cream can also be used daily to restore moisture and softness to areas of the face and body not being treated by laser or IPL.
• Ingredients: water (aqua), glycine soja (soybean) oil, cetyl alcohol, glycerin dimethicone, butyrospermum parkii (shea butter), theobroma cacao (cocoa) seed butter, aloe barbadensis (aloe vera) leaf juice, tocopheryl acetate, sodium ascorbyl phosphate, disodium EDTA, ceteareth-20, carbomer, BHT, benzyl benzoate, butylphenyl methylpropional, hexyl cinnamal, linalool, glyceryl caprylate, methylisothiazolinone. May contain: Red 4 (CI 14700, aka 504), Yellow 5 (CI 19140, Ki4), Yellow 6 (CI 15985, KI5), Blue 1 (CI 42090, Ao1), Red 33 (CI 17200, Aka 227), Ext. Violet 2 (CI 60730, Murasaki401), Green 3 (CI 42053, Midori3)
• Against Animal Testing
• Manufactured in Australia
• www.velvetglowclinic.com.au
• 500ml
• Pure Halo Laser Hair Removal logo (see attached files)
Nice to have
• A sophisticated and elegant design
Should not have
• no photos. not too many different colours

```html
<!DOCTYPE html>
<html lang="en">
<head>
<meta charset="utf-8">
<title>Pure Halo – Post Laser Calming Cream Label</title>
<link rel="stylesheet" href="https://fonts.googleapis.com/css2?family=Abel&family=Noto+Serif:ital,wght@1,400&family=Raleway:wght@500&family=Oswald:wght@500&display=swap">
<style>
  :root {
    --label-green: #dcecd2;
    --label-green-light: #e4f1dc;
    --ink: #3d423d;
    --ink-soft: #4d544d;
    --accent-green: #7cc47a;
  }
  * { margin: 0; padding: 0; box-sizing: border-box; }
  html, body {
    width: 741px;
    height: 1200px;
    overflow: hidden;
  }
  body {
    background: linear-gradient(180deg, var(--label-green-light) 0%, var(--label-green) 100%);
    color: var(--ink);
    position: relative;
  }
  .label {
    position: absolute;
    left: 92px;
    top: 128px;
    width: 560px;
  }
  .brand-name {
    font-family: "Raleway", sans-serif;
    font-weight: 500;
    font-size: 66px;
    line-height: 1;
    letter-spacing: -1px;
    color: var(--ink);
  }
  .brand-tagline {
    margin-top: 10px;
    font-family: "Abel", sans-serif;
    font-size: 27px;
    letter-spacing: 5px;
    color: var(--ink-soft);
  }
  .product-type {
    margin-top: 118px;
    font-family: "Abel", sans-serif;
    font-size: 31px;
    letter-spacing: 5px;
    color: var(--ink-soft);
  }
  .product-name {
    margin-top: 124px;
    font-family: "Oswald", sans-serif;
    font-weight: 500;
    font-size: 24px;
    line-height: 42px;
    letter-spacing: 3px;
    color: var(--ink);
  }
  .product-description {
    margin-top: 58px;
    width: 400px;
    font-family: "Abel", sans-serif;
    font-size: 25px;
    line-height: 32px;
    color: var(--ink-soft);
  }
  .directions {
    margin-top: 50px;
    padding-left: 16px;
    border-left: 3px solid var(--accent-green);
    font-family: "Noto Serif", serif;
    font-style: italic;
    font-size: 23px;
    line-height: 32px;
    letter-spacing: 2.5px;
    color: var(--ink-soft);
    margin-left: 4px;
  }
  .volume {
    margin-top: 128px;
    font-family: "Oswald", sans-serif;
    font-weight: 500;
    font-size: 19px;
    letter-spacing: 2px;
    color: var(--ink-soft);
  }
</style>
</head>
<body>
  <main class="label">
    <h1 class="brand-name">PURE HALO</h1>
    <p class="brand-tagline">LASER HAIR REMOVAL</p>

    <p class="product-type">BODY LOTION</p>

    <h2 class="product-name">POST LASER<br>CALMING CREAM</h2>

    <p class="product-description">Fresh Cucumber, Melon and Aloe Vera Leaf Juice blend together in perfect harmony to quickly cool you skin and restore your skins natural moisture.</p>

    <p class="directions">Use a liberal amount<br>twice daily on all<br>your treatment areas.</p>

    <p class="volume">500ML</p>
  </main>
</body>
</html>
```